Quorvex - Automated robotic Inspection with AI need new business cards

We need a new design of our business cards. The company is focused on automated quality control at high speed with unmatched results. We have a logo but need a more forward leaning business card that shows that we are delivering cutting edge technology.

Contact Information for Business Card

Name
Position
Adress
Phone
Email
e.g.
Lena Holmqvist
Chief Financial Officer (CFO)

Quorvex Sweden AB
Bruksvägen 14, SE-175 43 JÄRFÄLLA, Sweden
Mobile: +46735 21 47 83 | Office: +46 8 61 94 27
www.quorvex-example.com

Font styles to use
Sans Serif

```html
<!DOCTYPE html>
<html lang="en">
<head>
<meta charset="utf-8">
<title>Quorvex Business Card</title>
<link href="https://fonts.googleapis.com/css2?family=Roboto:wght@400;500;700&display=swap" rel="stylesheet">
<style>
  :root {
    --brand: #1b5882;
    --ink: #111111;
    --ink-soft: #2a2a2a;
    --paper: #ffffff;
    --edge: #6f6f6f;
  }
  * { box-sizing: border-box; margin: 0; padding: 0; }
  html, body {
    width: 1200px; height: 1200px; overflow: hidden;
    background: var(--paper);
    font-family: "Roboto", Arial, sans-serif;
  }
  .stage { position: relative; width: 1200px; height: 1200px; }
  .card {
    position: absolute;
    width: 883px; height: 540px;
    background: var(--paper);
    border: 1px solid var(--edge);
    overflow: hidden;
  }
  .card--front { left: 160px; top: 42px; }
  .card--back { left: 164px; top: 626px; }

  /* Front */
  .name-bar {
    position: absolute; left: 0; right: 0; top: 72px; height: 43px;
    display: flex; align-items: center;
  }
  .name-bar__block { height: 43px; background: var(--brand); }
  .name-bar__block--lead { width: 62px; flex: none; }
  .name-bar__block--tail { flex: 1; }
  .person-name {
    padding: 0 16px 0 18px;
    font-weight: 700; font-size: 41px; line-height: 43px;
    color: var(--brand); letter-spacing: -0.3px; white-space: nowrap;
  }
  .person-title {
    position: absolute; left: 80px; top: 114px;
    font-weight: 500; font-size: 21px; color: var(--ink-soft);
    letter-spacing: 0.2px;
  }
  .address {
    position: absolute; left: 80px; top: 198px;
    font-style: normal; font-weight: 400; font-size: 27px; line-height: 33px;
    color: var(--ink);
  }
  .contacts {
    position: absolute; left: 46px; top: 359px; list-style: none;
  }
  .contacts__item {
    display: flex; align-items: center; height: 37px;
    font-size: 28px; font-weight: 500; color: var(--ink);
  }
  .contacts__icon { width: 29px; height: 29px; margin-right: 11px; flex: none; }
  .brand-name {
    position: absolute; left: 498px; top: 378px; width: 360px;
    display: flex; align-items: center; justify-content: center; gap: 14px;
    font-weight: 700; font-size: 62px; color: var(--brand); letter-spacing: 2px;
  }
  .brand-name__dot { width: 30px; height: 30px; border-radius: 50%; background: var(--brand); flex: none; }

  /* Back */
  .brand-name--large {
    left: 0; width: 100%; top: 196px;
    font-size: 98px; gap: 22px; letter-spacing: 3px;
  }
  .brand-name--large .brand-name__dot { width: 46px; height: 46px; }
  .web-bar {
    position: absolute; left: 0; right: 0; top: 424px; height: 43px;
    background: var(--brand);
    display: flex; align-items: center; justify-content: center;
    font-weight: 500; font-size: 26px; color: var(--paper);
  }
</style>
</head>
<body>
<div class="stage">
  <section class="card card--front">
    <div class="name-bar">
      <div class="name-bar__block name-bar__block--lead"></div>
      <h1 class="person-name">LENA HOLMQVIST</h1>
      <div class="name-bar__block name-bar__block--tail"></div>
    </div>
    <p class="person-title">CHIEF FINANCIAL OFFICER (CFO)</p>
    <address class="address">
      Quorvex Sweden AB,<br>
      Bruksvägen 14, SE-175 43 JÄRFÄLLA,<br>
      Sweden
    </address>
    <ul class="contacts">
      <li class="contacts__item">
        <svg class="contacts__icon" viewBox="0 0 30 30" aria-hidden="true">
          <circle cx="15" cy="15" r="15" fill="var(--brand)"/>
          <rect x="10.5" y="7" width="9" height="16" rx="1.5" fill="none" stroke="#fff" stroke-width="1.6"/>
          <rect x="12.5" y="9.5" width="5" height="7" fill="#fff"/>
          <circle cx="15" cy="20" r="1" fill="#fff"/>
        </svg>
        +46735 21 47 83
      </li>
      <li class="contacts__item">
        <svg class="contacts__icon" viewBox="0 0 30 30" aria-hidden="true">
          <circle cx="15" cy="15" r="15" fill="var(--brand)"/>
          <path d="M10 8.5c1-.6 1.8-.4 2.3.5l1.3 2.4c.4.8.2 1.5-.5 2l-.9.6c.7 1.7 2 3 3.6 3.8l.7-.9c.5-.7 1.3-.8 2-.4l2.3 1.4c.8.5 1 1.4.4 2.3-1 1.5-2.5 2-4.2 1.4-4.2-1.5-7.2-4.6-8.6-8.8-.5-1.7 0-3.3 1.6-4.3z" fill="#fff"/>
        </svg>
        +46 8 61 94 27
      </li>
      <li class="contacts__item">
        <svg class="contacts__icon" viewBox="0 0 30 30" aria-hidden="true">
          <circle cx="15" cy="15" r="15" fill="var(--brand)"/>
          <rect x="7.5" y="10" width="15" height="10" rx="1" fill="none" stroke="#fff" stroke-width="1.6"/>
          <path d="M7.8 10.5 15 16l7.2-5.5M7.8 19.5l5.2-4.5M22.2 19.5 17 15" fill="none" stroke="#fff" stroke-width="1.4"/>
        </svg>
        lena@quorvex-example.com
      </li>
    </ul>
    <div class="brand-name"><span class="brand-name__dot"></span>QUORVEX</div>
  </section>

  <section class="card card--back">
    <div class="brand-name brand-name--large"><span class="brand-name__dot"></span>QUORVEX</div>
    <div class="web-bar">www.quorvex-example.com</div>
  </section>
</div>
</body>
</html>
```